Best in class cloud software provider for retailers needs a new business card design to reflect prod

We are a software company based out of Chicago selling into retailers. We have a new website and marketing collateral that support our new product designs. We are obsessed with simplicity, ease of use, and having a really powerful product set. We have two products as noted on our website - www.plumvector.example - one is a retail task management product and the other is a Help Ticketing product.

At PlumVector we are passionate about creating the best Retail Task Management system in the industry. We bring more than 20 years of retail operations, Workforce Management and Retail Task experience and have a set of web and mobile software features that no one else has. PlumVector enables you to plan and distribute work throughout your organization and ensure it gets done.

We need a new business card design that reflects our new branding, message and approach.

I've attached a few documents that help support what we are building and how our colors look.

There may be additional future work if this goes well.

Thanks,
Brian

President

Target Market(s)

We sell into retailers and are a software company

Industry/Entity Type

Software

Contact Information for Business Card

The card must have

Name
title
address
tele
email
PlumVector logo (someplace)

So for example

It would have for me

Brian Okafor
President
47 North Garnet Ave. Suite 310
Chicago, IL 60618
3127814063
bokafor@plumvector.example

Requirements
Must have
• We need to cards for 5 different people - same design different names etc
Nice to have
• should reflect our colors and product and website - be creative - ease of use, simplicity, and power is what the product is about - but we are very forward PlumVector and hear all the time that our product is gorgeous. The font should be consistent with our website, and marketing one pager included
Should not have
• Strange or unfamiliar colors or fonts...

```html
<!DOCTYPE html>
<html lang="en">
<head>
<meta charset="utf-8">
<title>PlumVector – Business Card</title>
<link href="https://fonts.googleapis.com/css2?family=Open+Sans:wght@400;600;700&display=swap" rel="stylesheet">
<style>
  :root {
    --backdrop: #3b3431;
    --card-black: #050505;
    --card-glow: #1f1f1f;
    --brand-orange: #f26a2a;
    --text-white: #f2f2f2;
    --tab-silver: #d9d9d9;
  }
  * { margin: 0; padding: 0; box-sizing: border-box; }
  html, body {
    width: 1200px; height: 844px; overflow: hidden;
    background: var(--backdrop);
    font-family: "Open Sans", Arial, sans-serif;
  }
  .stage {
    position: relative; width: 1200px; height: 844px;
    display: flex; align-items: center; justify-content: center; gap: 60px;
  }
  .card {
    position: relative; width: 510px; height: 292px;
    background: var(--card-black);
    box-shadow: 0 14px 30px rgba(0,0,0,0.45);
    overflow: hidden;
  }

  /* Contact side */
  .card--contact {
    background: linear-gradient(90deg, var(--card-black) 0%, #0b0b0b 60%, var(--card-glow) 100%);
  }
  .band {
    position: absolute; left: 0; right: 0; height: 11px;
    background: var(--brand-orange);
  }
  .band--top { top: 12px; }
  .band--bottom { bottom: 12px; }
  .contact {
    position: absolute; left: 230px; top: 52px; width: 250px;
    color: var(--text-white); text-align: center;
  }
  .contact__name {
    display: inline-block;
    font-weight: 600; font-size: 17px; letter-spacing: 0.5px;
    color: var(--brand-orange); text-transform: uppercase;
    padding: 0 6px 3px; border-bottom: 1px solid var(--brand-orange);
  }
  .contact__title { font-size: 12px; margin-top: 4px; }
  .contact__lines { margin-top: 34px; font-size: 13px; line-height: 1.75; }
  .contact__address { margin-top: 30px; font-size: 13px; }

  /* Logo side */
  .card--logo {
    background: radial-gradient(ellipse at 52% 38%, #2a2a2a 0%, #101010 45%, var(--card-black) 80%);
  }
  .tab {
    position: absolute; width: 26px; height: 38px;
    background: var(--brand-orange);
  }
  .tab--top { right: 0; top: 26px; border-left: 4px solid var(--tab-silver); }
  .tab--bottom { left: 0; top: 166px; border-right: 4px solid var(--tab-silver); }
  .brand-name {
    position: absolute; left: 0; right: 0; top: 118px;
    text-align: center;
    font-weight: 700; font-size: 50px; letter-spacing: -0.5px;
    color: var(--brand-orange);
  }
</style>
</head>
<body>
  <main class="stage">
    <section class="card card--contact" aria-label="Business card, contact side">
      <div class="band band--top"></div>
      <div class="contact">
        <div class="contact__name">Brian Okafor</div>
        <div class="contact__title">President</div>
        <div class="contact__lines">
          <div>3127814063</div>
          <div>bokafor@plumvector.example</div>
        </div>
        <div class="contact__address">47 North Garnet Ave. Suite 310 Chicago, IL 60618</div>
      </div>
      <div class="band band--bottom"></div>
    </section>

    <section class="card card--logo" aria-label="Business card, brand side">
      <div class="tab tab--top"></div>
      <div class="brand-name">PlumVector</div>
      <div class="tab tab--bottom"></div>
    </section>
  </main>
</body>
</html>
```